QR TILL WORKS , CREDIT CARD PROCESSING EQUIPMENT

qrtillworks is a sub division of Tallow a credit car processing co.
dorian vale
14 cedar hollow ln
elmbrook qv 07312
suite 412

qrtillworks.example
cell 555-214-7730
office 555-861-2093
we sell pos systems to merchant who want to accept credit cards at there retail location.
black card would be nice buit open to different ideas

Target Market(s)

retail merchants

Industry/Entity Type

credit card processing

Contact Information for Business Card

card should include web site phone address

Colors

Designer to choose colors to be used in the design.

Requirements
Should not have
• red

```html
<!DOCTYPE html>
<html lang="en">
<head>
<meta charset="utf-8">
<title>QR Till Works – Business Card</title>
<link rel="stylesheet" href="https://fonts.googleapis.com/css2?family=Open+Sans:wght@400;600&display=swap">
<style>
  :root {
    --backdrop: #2e2e30;
    --card: #1c1d1f;
    --ink: #f4f4f4;
    --muted: #c9c9c9;
    --accent: #f2c21b;
    --rule: #55575b;
  }
  * { box-sizing: border-box; margin: 0; padding: 0; }
  html, body { width: 1200px; height: 1108px; overflow: hidden; }
  body {
    background: var(--backdrop);
    font-family: "Open Sans", Arial, sans-serif;
    position: relative;
  }
  .card {
    position: absolute;
    top: 224px;
    width: 420px;
    height: 660px;
    border-radius: 26px;
    background: var(--card);
    box-shadow: 0 18px 40px rgba(0,0,0,.45);
    overflow: hidden;
  }
  .card--front { left: 150px; }
  .card--back { left: 630px; }

  /* front */
  .brand {
    position: absolute;
    top: 150px;
    left: 0; right: 0;
    display: flex;
    align-items: center;
    justify-content: center;
    gap: 12px;
  }
  .brand__dot {
    width: 16px; height: 16px;
    border-radius: 50%;
    background: var(--accent);
  }
  .brand__name {
    color: var(--ink);
    font-weight: 600;
    font-size: 40px;
    letter-spacing: 1px;
  }
  .holder {
    position: absolute;
    top: 392px; left: 0; right: 0;
    text-align: center;
    color: var(--accent);
    font-weight: 600;
    font-size: 30px;
  }
  .divider {
    position: absolute;
    left: 70px; right: 70px;
    height: 1px;
    background: var(--rule);
  }
  .divider--icons { top: 458px; }
  .divider--address { top: 574px; }
  .icons {
    position: absolute;
    top: 444px; left: 0; right: 0;
    display: flex;
    justify-content: center;
    gap: 6px;
  }
  .icon {
    width: 28px; height: 28px;
    border-radius: 4px;
    background: var(--accent);
    border: 2px solid var(--card);
    outline: 1px solid var(--accent);
    display: flex; align-items: center; justify-content: center;
  }
  .contact {
    position: absolute;
    top: 484px; left: 0; right: 0;
    text-align: center;
    color: var(--ink);
    font-size: 17px;
    line-height: 26px;
  }
  .contact__site-name { color: var(--accent); }
  .address {
    position: absolute;
    top: 584px; left: 0; right: 0;
    text-align: center;
    color: var(--muted);
    font-size: 16px;
    line-height: 24px;
  }

  /* back */
  .back-pattern {
    position: absolute;
    inset: 0;
    background:
      repeating-linear-gradient(-22deg, rgba(255,255,255,0.00) 0 38px, rgba(255,255,255,0.045) 38px 60px),
      linear-gradient(160deg, #1e1f22, #161719 60%, #232427);
  }
  .back-brand {
    position: absolute;
    top: 312px; left: 0; right: 0;
    display: flex;
    align-items: center;
    justify-content: center;
    gap: 10px;
  }
  .back-brand .brand__name { font-size: 32px; }
  .back-brand .brand__dot { width: 13px; height: 13px; }
</style>
</head>
<body>

<section class="card card--front">
  <div class="brand">
    <span class="brand__name">QR TILL WORKS</span>
    <span class="brand__dot"></span>
  </div>

  <p class="holder">Dorian Vale</p>

  <div class="divider divider--icons"></div>
  <div class="icons">
    <span class="icon" aria-label="phone">
      <svg width="16" height="16" viewBox="0 0 16 16"><path d="M3 2h3l1 3-2 1c1 2 2 3 4 4l1-2 3 1v3c0 1-1 2-2 2C6 14 2 10 2 4c0-1 0-2 1-2z" fill="#1c1d1f"/></svg>
    </span>
    <span class="icon" aria-label="email">
      <svg width="16" height="16" viewBox="0 0 16 16"><rect x="2" y="4" width="12" height="8" fill="#1c1d1f"/><path d="M2 4l6 5 6-5" fill="none" stroke="#f2c21b" stroke-width="1.2"/></svg>
    </span>
    <span class="icon" aria-label="website">
      <svg width="16" height="16" viewBox="0 0 16 16"><circle cx="8" cy="8" r="6" fill="#1c1d1f"/><path d="M2 8h12M8 2c-3 3-3 9 0 12M8 2c3 3 3 9 0 12" fill="none" stroke="#f2c21b" stroke-width="1"/></svg>
    </span>
  </div>

  <div class="contact">
    <p>555-214-7730</p>
    <p>555-861-2093</p>
    <p>www.<span class="contact__site-name">qrtillworks</span>.example</p>
  </div>

  <div class="divider divider--address"></div>
  <div class="address">
    <p>14 cedar hollow ln</p>
    <p>elmbrook qv 07312, suite 412</p>
  </div>
</section>

<section class="card card--back">
  <div class="back-pattern" role="img" aria-label="Tone-on-tone repeating brand pattern across the card back"></div>
  <div class="back-brand">
    <span class="brand__name">QR TILL WORKS</span>
    <span class="brand__dot"></span>
  </div>
</section>

</body>
</html>
```